Front book cover for a training course to help bakers get higher prices and sell more wedding cakes.

We need a front cover for a book that will be teaching bakers how to sell wedding cakes to get higher prices and book more orders. It is a business book. Do not make it look like we want brides to read it. Bakers will be judging the cover to see if it is worth their investment to read it. The title is already in the logo, so do not repeat it.

Target Market(s)

Bakers who sell wedding cakes

Industry/Entity Type

Bakery

Colors

Designer to choose colors to be used in the design.

Requirements
Must have
• Must use the logo. Must have author name: Lou Brand. Must have subtitle: Raise Your Rates. Win More Couples. Grow Your Bakery.
Nice to have
• You are free to be creative. The concept is not to be pretty. It is a business sales and marketing book

```html
<!DOCTYPE html>
<html lang="en">
<head>
<meta charset="utf-8">
<title>Tiered Profit Academy – Book Cover</title>
<link href="https://fonts.googleapis.com/css2?family=Russo+One&family=Josefin+Sans:wght@300;600&display=swap" rel="stylesheet">
<style>
  :root {
    --backdrop: #8a8a8a;
    --marble-white: #fbfafb;
    --marble-vein: #d9d7da;
    --panel: rgba(255,255,255,0.6);
    --gold: #d4a53c;
    --gold-light: #f0d98a;
    --ink-dark: #54565a;
    --tagline: #a88663;
    --accent-pink: #ec4a74;
  }
  * { margin: 0; padding: 0; box-sizing: border-box; }
  html, body {
    width: 1075px; height: 1200px; overflow: hidden;
    background: var(--backdrop);
  }
  .book-cover {
    position: absolute; left: 189px; top: 74px;
    width: 705px; height: 1057px;
    background:
      radial-gradient(ellipse 260px 180px at 10% 20%, var(--marble-vein), transparent 70%),
      radial-gradient(ellipse 220px 300px at 95% 45%, var(--marble-vein), transparent 70%),
      radial-gradient(ellipse 300px 200px at 20% 75%, #e3e1e4, transparent 70%),
      radial-gradient(ellipse 260px 160px at 85% 95%, var(--marble-vein), transparent 70%),
      var(--marble-white);
    overflow: hidden;
  }
  .corner-lines { position: absolute; inset: 0; }
  .inner-panel {
    position: absolute; left: 65px; top: 70px; width: 576px; height: 919px;
    background: var(--panel);
  }
  .gold-frame {
    position: absolute; left: 42px; top: 47px; width: 619px; height: 963px;
    border: 2px solid var(--gold);
  }
  .ornament-band {
    position: absolute; left: 44px; width: 615px; height: 97px;
    background: radial-gradient(ellipse at 50% 50%, var(--gold-light), rgba(212,165,60,0.35) 60%, rgba(212,165,60,0.15));
  }
  .ornament-top { top: 49px; }
  .ornament-bottom { top: 911px; }
  .brand-mark {
    position: absolute; left: 0; width: 100%; top: 180px;
    text-align: center;
  }
  .brand-dot {
    display: block; margin: 0 auto 44px;
    width: 100px; height: 100px; border-radius: 50%;
    background: var(--accent-pink);
  }
  .brand-name {
    font-family: "Russo One", sans-serif;
    color: var(--ink-dark);
    font-size: 64px; line-height: 76px;
  }
  .gold-rule {
    position: absolute; left: 257px; width: 191px; height: 2px;
    background: linear-gradient(90deg, rgba(212,165,60,0.2), var(--gold), rgba(212,165,60,0.2));
  }
  .rule-upper { top: 560px; }
  .rule-lower { top: 823px; }
  .subtitle-line {
    position: absolute; left: 0; width: 100%;
    text-align: center;
    font-family: "Josefin Sans", sans-serif; font-weight: 300;
    font-size: 33px; letter-spacing: 0.28em;
    color: var(--tagline);
    line-height: 40px;
  }
  .line-1 { top: 590px; }
  .line-2 { top: 672px; }
  .line-3 { top: 753px; }
  .heart-icon {
    position: absolute; left: 340px; width: 24px; height: 22px;
  }
  .heart-1 { top: 642px; }
  .heart-2 { top: 724px; }
  .author-name {
    position: absolute; left: 0; width: 100%; top: 855px;
    text-align: center;
    font-family: "Josefin Sans", sans-serif; font-weight: 600;
    font-size: 34px; letter-spacing: 0.3em;
    color: var(--accent-pink);
  }
</style>
</head>
<body>
  <div class="book-cover">
    <svg class="corner-lines" width="705" height="1057" viewBox="0 0 705 1057">
      <g stroke="#e3c57a" stroke-width="1" fill="none">
        <line x1="0" y1="170" x2="195" y2="0"/>
        <line x1="0" y1="180" x2="210" y2="0"/>
        <line x1="705" y1="170" x2="510" y2="0"/>
        <line x1="705" y1="180" x2="495" y2="0"/>
        <line x1="0" y1="887" x2="195" y2="1057"/>
        <line x1="0" y1="877" x2="210" y2="1057"/>
        <line x1="705" y1="887" x2="510" y2="1057"/>
        <line x1="705" y1="877" x2="495" y2="1057"/>
      </g>
    </svg>
    <div class="inner-panel"></div>
    <div class="gold-frame"></div>
    <div class="ornament-band ornament-top" role="img" aria-label="Gold filigree ornament border along the top"></div>
    <div class="ornament-band ornament-bottom" role="img" aria-label="Gold filigree ornament border along the bottom"></div>

    <div class="brand-mark">
      <span class="brand-dot"></span>
      <div class="brand-name">Tiered Profit<br>Academy</div>
    </div>

    <div class="gold-rule rule-upper"></div>
    <p class="subtitle-line line-1">Raise Your Rates.</p>
    <svg class="heart-icon heart-1" viewBox="0 0 16 15"><path d="M8 15 L1.5 8.3 A4 4 0 0 1 8 2.8 A4 4 0 0 1 14.5 8.3 Z" fill="#ec4a74"/></svg>
    <p class="subtitle-line line-2">Win More Couples.</p>
    <svg class="heart-icon heart-2" viewBox="0 0 16 15"><path d="M8 15 L1.5 8.3 A4 4 0 0 1 8 2.8 A4 4 0 0 1 14.5 8.3 Z" fill="#ec4a74"/></svg>
    <p class="subtitle-line line-3">Grow Your Bakery.</p>
    <div class="gold-rule rule-lower"></div>

    <p class="author-name">Lou Brand</p>
  </div>
</body>
</html>
```